How likely are people to engage in social distancing? We need a good illustration to show the data!

We surveyed U.S. adults March 20th - 24th, 2020 and asked how likely they were to engage in social distancing (and other COVID-19 related health behaviors). What did the survey find? Basically, most people intend to engage in social distancing behaviors (e.g., avoiding large crowds) and other behaviors that reduce the spread of COVID-19 (e.g., washing hands at least 20 seconds). When most people intend to engage in a behavior, then public health professionals try to leverage that to move more people to act.
Now we need innovative and professional images that attempt to communicate one or all of these findings. The specific findings are nicely summarized in the attached document. For example, 82% of participants intend to engage in social distancing.
What sort of visual are we looking for? Our preference is for an original illustration (or set of illustrations). Our preference is for (creative and powerful illustrations, but we are also open to the creative and well-executed infographics.
We need these images fast . We will award monetary prizes to the 3 best designs. If we like more than that, then we might purchase more (e.g., in past contests, we have purchased as many as 30 designs).
What we will need:
(1) The illustrations must be original and we will need the photoshop and/or illustrator files for all artwork.
(2) You can illustrate all of the findings or just one of them. We need creative approaches that do a lucid job of bringing the data to life. Most people intend to engage in these behaviors. How to communicate that? Corvantists and Halmerites do not differ in their intentions; how to communicate that?
(3) The illustration should say, somewhere: "Based on a survey of 400 U.S. adults conducted March 20 - 24th, 2020."

U.S. Adults

• Original illustrations based on the findings of the survey (see attached document).

```html
<!DOCTYPE html>
<html lang="en">
<head>
<meta charset="utf-8">
<title>How Likely Are People to Engage in Social Distancing</title>
<link href="https://fonts.googleapis.com/css2?family=Arimo:ital,wght@0,400;0,700;1,700&family=Nunito:wght@900&family=Roboto+Slab:wght@800&display=swap" rel="stylesheet">
<style>
  :root{
    --bg:#42182f;
    --bg-deep:#2f0f22;
    --ink:#ffffff;
    --ink-soft:#f1e6ec;
    --card-top:#8f3563;
    --card-mid:#c07e9e;
    --card-bottom:#ead0db;
    --pie-top:#a3195b;
    --pie-side:#6d0a3f;
    --pie-grey:#c9c9c9;
    --pie-grey-side:#8a8a8a;
    --rep:#c3077a;
    --rep-side:#8e0050;
    --rep-cap:#e0449c;
    --dem:#2a2b8c;
    --dem-side:#18145a;
    --dem-cap:#4a4cb3;
  }
  *{margin:0;padding:0;box-sizing:border-box}
  html,body{width:1200px;height:2357px;overflow:hidden}
  body{
    position:relative;
    background:radial-gradient(circle at 70% 20%, #4d1c37 0%, var(--bg) 45%, var(--bg-deep) 100%);
    color:var(--ink);
    font-family:"Arimo",Arial,sans-serif;
  }
  .title{
    position:absolute;left:0;top:40px;width:1200px;text-align:center;
    font-family:"Roboto Slab",Georgia,serif;font-weight:800;
    font-size:47px;line-height:57px;letter-spacing:2px;text-transform:uppercase;white-space:nowrap;
  }
  .intro{
    position:absolute;left:48px;top:186px;width:1110px;
    font-size:26px;line-height:33.5px;color:var(--ink-soft);
  }
  .section-head{
    position:absolute;left:0;width:1200px;text-align:center;font-weight:700;
  }
  .findings-head{top:546px;font-size:42px}
  .rule{position:absolute;height:2px;background:var(--ink)}
  .card{
    position:absolute;width:245px;height:360px;
    border-radius:30px 30px 100px 100px;
    background:linear-gradient(180deg,var(--card-top) 0%,var(--card-mid) 55%,var(--card-bottom) 100%);
  }
  .card h3{
    position:absolute;left:0;top:10px;width:100%;text-align:center;
    font-family:"Nunito","Arial Rounded MT Bold",sans-serif;font-weight:900;
    font-size:23px;line-height:28px;color:var(--ink);
  }
  .card h3.small{font-size:19px;line-height:23px;top:12px}
  .card .art{
    position:absolute;left:28px;top:72px;width:189px;height:112px;border-radius:14px;
    background:radial-gradient(ellipse at 50% 45%, rgba(255,255,255,.28), rgba(255,255,255,.06) 70%);
  }
  .card svg{position:absolute;left:0;top:0}
  .pct{font-family:"Nunito",sans-serif;font-weight:900;font-size:44px;fill:#fff;stroke:#7a7a7a;stroke-width:1.5;paint-order:stroke}
  .compare-head{top:1472px;font-size:46px}
  .compare-sub{position:absolute;left:0;top:1531px;width:1200px;text-align:center;font-size:35px}
  .chart{position:absolute;left:0;top:0}
  .axis-label{font-family:"Arimo",sans-serif;font-weight:700;font-size:26px;fill:#fff}
  .bar-label{font-family:"Arimo",sans-serif;font-weight:700;font-style:italic;font-size:16px;fill:#fff}
  .cat{position:absolute;top:2133px;width:120px;text-align:center;font-size:19px;line-height:21px;color:var(--ink-soft)}
  .cat.small{font-size:15.5px;line-height:20px}
  .legend{position:absolute;top:2234px;display:flex;align-items:center;font-size:22px;color:var(--ink-soft)}
  .swatch{width:64px;height:28px;margin-right:11px}
  .footnote{position:absolute;left:0;top:2308px;width:1200px;text-align:center;font-size:22px;color:var(--ink-soft)}
</style>
</head>
<body>

<h1 class="title">How likely are people to engage in<br>social distancing</h1>

<p class="intro">
We surveyed 400 U.S. adults from March 20th – 24th, 2020 and asked how likely they<br>
were to engage in<br>
social distancing (and other COVID-19 related health behaviors).<br><br>
What did the survey find?<br>
Basically, most people intend to engage in social distancing<br>
(e.g. avoiding large crowds) and other behaviors that reduce the spread of COVID-19<br>
(e.g. washing hands at least 20 seconds).<br>
When most people intend to engage in a behavior, then public health professionals try<br>
to leverage that to move more people to act.
</p>

<div class="rule" style="left:29px;top:572px;width:280px"></div>
<h2 class="section-head findings-head">What did the Survey find?</h2>
<div class="rule" style="left:318px;top:603px;width:564px;height:4px"></div>
<div class="rule" style="left:891px;top:572px;width:280px"></div>

<svg width="0" height="0" style="position:absolute">
  <defs>
    <linearGradient id="pieTop" x1="0" y1="0" x2="0" y2="1"><stop offset="0" stop-color="#8e1250"/><stop offset="1" stop-color="#a81d60"/></linearGradient>
    <linearGradient id="greySide" x1="0" y1="0" x2="1" y2="0"><stop offset="0" stop-color="#9a9a9a"/><stop offset="1" stop-color="#6f6f6f"/></linearGradient>
  </defs>
</svg>

<!-- Row 1 -->
<div class="card" style="left:48px;top:649px">
  <h3>Engage in<br>Social Distancing</h3>
  <div class="art" role="img" aria-label="Three figures standing six feet apart with arrows between them"></div>
  <svg width="245" height="360">
    <path d="M18 254 A104 58 0 0 0 226 254 L226 291 A104 58 0 0 1 18 291 Z" fill="var(--pie-side)"/>
    <path d="M122 312 A104 58 0 0 1 27.9 278.7 L27.9 315.7 A104 58 0 0 0 122 349 Z" fill="url(#greySide)"/>
    <ellipse cx="122" cy="254" rx="104" ry="58" fill="url(#pieTop)"/>
    <path d="M122 254 L122 312 A104 58 0 0 1 27.9 278.7 Z" fill="var(--pie-grey)"/>
    <text class="pct" x="135" y="247" text-anchor="middle">82%</text>
  </svg>
</div>

<div class="card" style="left:335px;top:649px">
  <h3>Work from<br>Home</h3>
  <div class="art" role="img" aria-label="Person working at a laptop on a desk with a lamp and a cup"></div>
  <svg width="245" height="360">
    <path d="M18 254 A104 58 0 0 0 226 254 L226 291 A104 58 0 0 1 18 291 Z" fill="var(--pie-side)"/>
    <path d="M122 312 A104 58 0 0 1 18 254 L18 291 A104 58 0 0 0 122 349 Z" fill="url(#greySide)"/>
    <ellipse cx="122" cy="254" rx="104" ry="58" fill="url(#pieTop)"/>
    <path d="M122 254 L122 312 A104 58 0 0 1 46.2 214.3 Z" fill="var(--pie-grey)"/>
    <text class="pct" x="135" y="247" text-anchor="middle">63%</text>
  </svg>
</div>

<div class="card" style="left:620px;top:649px">
  <h3>Avoid Large<br>Gatherings</h3>
  <div class="art" role="img" aria-label="Large crowd of small figures"></div>
  <svg width="245" height="360">
    <path d="M18 254 A104 58 0 0 0 226 254 L226 291 A104 58 0 0 1 18 291 Z" fill="var(--pie-side)"/>
    <path d="M122 312 A104 58 0 0 1 37.9 288.1 L37.9 325.1 A104 58 0 0 0 122 349 Z" fill="url(#greySide)"/>
    <ellipse cx="122" cy="254" rx="104" ry="58" fill="url(#pieTop)"/>
    <path d="M122 254 L122 312 A104 58 0 0 1 37.9 288.1 Z" fill="var(--pie-grey)"/>
    <text class="pct" x="135" y="247" text-anchor="middle">85%</text>
  </svg>
</div>

<div class="card" style="left:905px;top:649px">
  <h3>Cancel<br>Social Activities</h3>
  <div class="art" role="img" aria-label="Group of friends standing arm in arm, seen from behind"></div>
  <svg width="245" height="360">
    <path d="M18 254 A104 58 0 0 0 226 254 L226 291 A104 58 0 0 1 18 291 Z" fill="var(--pie-side)"/>
    <path d="M122 312 A104 58 0 0 1 25.3 275.4 L25.3 312.4 A104 58 0 0 0 122 349 Z" fill="url(#greySide)"/>
    <ellipse cx="122" cy="254" rx="104" ry="58" fill="url(#pieTop)"/>
    <path d="M122 254 L122 312 A104 58 0 0 1 25.3 275.4 Z" fill="var(--pie-grey)"/>
    <text class="pct" x="135" y="247" text-anchor="middle">81%</text>
  </svg>
</div>

<!-- Row 2 -->
<div class="card" style="left:48px;top:1055px">
  <h3 class="small">Put distance between<br>yourself &amp; others</h3>
  <div class="art" role="img" aria-label="Group of figures standing six feet away from one person"></div>
  <svg width="245" height="360">
    <path d="M18 254 A104 58 0 0 0 226 254 L226 291 A104 58 0 0 1 18 291 Z" fill="var(--pie-side)"/>
    <path d="M122 312 A104 58 0 0 1 37.9 288.1 L37.9 325.1 A104 58 0 0 0 122 349 Z" fill="url(#greySide)"/>
    <ellipse cx="122" cy="254" rx="104" ry="58" fill="url(#pieTop)"/>
    <path d="M122 254 L122 312 A104 58 0 0 1 37.9 288.1 Z" fill="var(--pie-grey)"/>
    <text class="pct" x="135" y="247" text-anchor="middle">85%</text>
  </svg>
</div>

<div class="card" style="left:335px;top:1055px">
  <h3>Wash Hands<br>atleast 20 Sec</h3>
  <div class="art" role="img" aria-label="Hands being washed with soap bubbles"></div>
  <svg width="245" height="360">
    <path d="M18 254 A104 58 0 0 0 226 254 L226 291 A104 58 0 0 1 18 291 Z" fill="var(--pie-side)"/>
    <path d="M122 312 A104 58 0 0 1 46.2 293.7 L46.2 330.7 A104 58 0 0 0 122 349 Z" fill="url(#greySide)"/>
    <ellipse cx="122" cy="254" rx="104" ry="58" fill="url(#pieTop)"/>
    <path d="M122 254 L122 312 A104 58 0 0 1 46.2 293.7 Z" fill="var(--pie-grey)"/>
    <text class="pct" x="135" y="247" text-anchor="middle">87%</text>
  </svg>
</div>

<div class="card" style="left:620px;top:1055px">
  <h3>Use<br>Hand Sanitizers</h3>
  <div class="art" role="img" aria-label="Pump bottle of hand sanitizer with a cross label"></div>
  <svg width="245" height="360">
    <path d="M18 254 A104 58 0 0 0 226 254 L226 291 A104 58 0 0 1 18 291 Z" fill="var(--pie-side)"/>
    <path d="M122 312 A104 58 0 0 1 37.9 288.1 L37.9 325.1 A104 58 0 0 0 122 349 Z" fill="url(#greySide)"/>
    <ellipse cx="122" cy="254" rx="104" ry="58" fill="url(#pieTop)"/>
    <path d="M122 254 L122 312 A104 58 0 0 1 37.9 288.1 Z" fill="var(--pie-grey)"/>
    <text class="pct" x="135" y="247" text-anchor="middle">85%</text>
  </svg>
</div>

<div class="card" style="left:905px;top:1055px">
  <h3 class="small" style="font-size:20px;line-height:24px">Avoid touching<br>Eyes, Nose &amp; Mouth</h3>
  <div class="art" role="img" aria-label="Prohibition sign over a nose, lips and an eye"></div>
  <svg width="245" height="360">
    <path d="M18 254 A104 58 0 0 0 226 254 L226 291 A104 58 0 0 1 18 291 Z" fill="var(--pie-side)"/>
    <path d="M122 312 A104 58 0 0 1 25.3 275.4 L25.3 312.4 A104 58 0 0 0 122 349 Z" fill="url(#greySide)"/>
    <ellipse cx="122" cy="254" rx="104" ry="58" fill="url(#pieTop)"/>
    <path d="M122 254 L122 312 A104 58 0 0 1 25.3 275.4 Z" fill="var(--pie-grey)"/>
    <text class="pct" x="135" y="247" text-anchor="middle">81%</text>
  </svg>
</div>

<!-- Comparison -->
<div class="rule" style="left:29px;top:1499px;width:116px"></div>
<h2 class="section-head compare-head">Comparing Corvantists and Halmerites</h2>
<div class="rule" style="left:1055px;top:1499px;width:116px"></div>
<p class="compare-sub">March 20th - 24th, 2020 Survey</p>
<div class="rule" style="left:344px;top:1583px;width:507px;height:4px"></div>

<svg class="chart" width="1200" height="2357">
  <g stroke="#fff" stroke-width="3" fill="none">
    <path d="M142 1637 L142 2125 L1114 2125"/>
    <path d="M142 1637 H181 M142 1734 H166 M142 1832 H166 M142 1929 H166 M142 2027 H166"/>
    <path d="M276 2125 v10 M396 2125 v10 M516 2125 v10 M636 2125 v10 M756 2125 v10 M875 2125 v10 M995 2125 v10 M1114 2125 v10"/>
  </g>
  <g text-anchor="end">
    <text class="axis-label" x="128" y="1646">100%</text>
    <text class="axis-label" x="128" y="1743">80%</text>
    <text class="axis-label" x="128" y="1841">60%</text>
    <text class="axis-label" x="128" y="1938">40%</text>
    <text class="axis-label" x="128" y="2036">20%</text>
    <text class="axis-label" x="128" y="2134">0%</text>
  </g>

  <!-- group: x, R top, D top -->
  <g transform="translate(212,0)">
    <rect x="-50" y="1722" width="35" height="400" fill="var(--rep)"/>
    <polygon points="-15,1722 14,1714 14,2122 -15,2122" fill="var(--rep-side)"/>
    <polygon points="-50,1722 -15,1722 14,1714 -21,1714" fill="var(--rep-cap)"/>
    <polygon points="5,1719 30,1727 30,2122 5,2122" fill="var(--dem-side)"/>
    <rect x="30" y="1727" width="30" height="395" fill="var(--dem)"/>
    <polygon points="5,1719 30,1727 60,1727 35,1719" fill="var(--dem-cap)"/>
    <text class="bar-label" transform="translate(-47,1742) rotate(15)">82%</text>
    <text class="bar-label" transform="translate(32,1745) rotate(-15)">81%</text>
  </g>
  <g transform="translate(338,0)">
    <rect x="-50" y="1829" width="35" height="293" fill="var(--rep)"/>
    <polygon points="-15,1829 14,1821 14,2122 -15,2122" fill="var(--rep-side)"/>
    <polygon points="-50,1829 -15,1829 14,1821 -21,1821" fill="var(--rep-cap)"/>
    <polygon points="5,1797 30,1805 30,2122 5,2122" fill="var(--dem-side)"/>
    <rect x="30" y="1805" width="30" height="317" fill="var(--dem)"/>
    <polygon points="5,1797 30,1805 60,1805 35,1797" fill="var(--dem-cap)"/>
    <text class="bar-label" transform="translate(-47,1849) rotate(15)">60%</text>
    <text class="bar-label" transform="translate(32,1823) rotate(-15)">65%</text>
  </g>
  <g transform="translate(457,0)">
    <rect x="-50" y="1707" width="35" height="415" fill="var(--rep)"/>
    <polygon points="-15,1707 14,1699 14,2122 -15,2122" fill="var(--rep-side)"/>
    <polygon points="-50,1707 -15,1707 14,1699 -21,1699" fill="var(--rep-cap)"/>
    <polygon points="5,1704 30,1712 30,2122 5,2122" fill="var(--dem-side)"/>
    <rect x="30" y="1712" width="30" height="410" fill="var(--dem)"/>
    <polygon points="5,1704 30,1712 60,1712 35,1704" fill="var(--dem-cap)"/>
    <text class="bar-label" transform="translate(-47,1727) rotate(15)">85%</text>
    <text class="bar-label" transform="translate(32,1730) rotate(-15)">84%</text>
  </g>
  <g transform="translate(576,0)">
    <rect x="-50" y="1722" width="35" height="400" fill="var(--rep)"/>
    <polygon points="-15,1722 14,1714 14,2122 -15,2122" fill="var(--rep-side)"/>
    <polygon points="-50,1722 -15,1722 14,1714 -21,1714" fill="var(--rep-cap)"/>
    <polygon points="5,1724 30,1732 30,2122 5,2122" fill="var(--dem-side)"/>
    <rect x="30" y="1732" width="30" height="390" fill="var(--dem)"/>
    <polygon points="5,1724 30,1732 60,1732 35,1724" fill="var(--dem-cap)"/>
    <text class="bar-label" transform="translate(-47,1742) rotate(15)">82%</text>
    <text class="bar-label" transform="translate(32,1750) rotate(-15)">80%</text>
  </g>
  <g transform="translate(695,0)">
    <rect x="-50" y="1712" width="35" height="410" fill="var(--rep)"/>
    <polygon points="-15,1712 14,1704 14,2122 -15,2122" fill="var(--rep-side)"/>
    <polygon points="-50,1712 -15,1712 14,1704 -21,1704" fill="var(--rep-cap)"/>
    <polygon points="5,1689 30,1697 30,2122 5,2122" fill="var(--dem-side)"/>
    <rect x="30" y="1697" width="30" height="425" fill="var(--dem)"/>
    <polygon points="5,1689 30,1697 60,1697 35,1689" fill="var(--dem-cap)"/>
    <text class="bar-label" transform="translate(-47,1732) rotate(15)">84%</text>
    <text class="bar-label" transform="translate(32,1715) rotate(-15)">87%</text>
  </g>
  <g transform="translate(815,0)">
    <rect x="-50" y="1697" width="35" height="425" fill="var(--rep)"/>
    <polygon points="-15,1697 14,1689 14,2122 -15,2122" fill="var(--rep-side)"/>
    <polygon points="-50,1697 -15,1697 14,1689 -21,1689" fill="var(--rep-cap)"/>
    <polygon points="5,1685 30,1693 30,2122 5,2122" fill="var(--dem-side)"/>
    <rect x="30" y="1693" width="30" height="429" fill="var(--dem)"/>
    <polygon points="5,1685 30,1693 60,1693 35,1685" fill="var(--dem-cap)"/>
    <text class="bar-label" transform="translate(-47,1717) rotate(15)">87%</text>
    <text class="bar-label" transform="translate(32,1711) rotate(-15)">88%</text>
  </g>
  <g transform="translate(935,0)">
    <rect x="-50" y="1697" width="35" height="425" fill="var(--rep)"/>
    <polygon points="-15,1697 14,1689 14,2122 -15,2122" fill="var(--rep-side)"/>
    <polygon points="-50,1697 -15,1697 14,1689 -21,1689" fill="var(--rep-cap)"/>
    <polygon points="5,1704 30,1712 30,2122 5,2122" fill="var(--dem-side)"/>
    <rect x="30" y="1712" width="30" height="410" fill="var(--dem)"/>
    <polygon points="5,1704 30,1712 60,1712 35,1704" fill="var(--dem-cap)"/>
    <text class="bar-label" transform="translate(-47,1717) rotate(15)">87%</text>
    <text class="bar-label" transform="translate(32,1730) rotate(-15)">84%</text>
  </g>
  <g transform="translate(1055,0)">
    <rect x="-50" y="1732" width="35" height="390" fill="var(--rep)"/>
    <polygon points="-15,1732 14,1724 14,2122 -15,2122" fill="var(--rep-side)"/>
    <polygon points="-50,1732 -15,1732 14,1724 -21,1724" fill="var(--rep-cap)"/>
    <polygon points="5,1714 30,1722 30,2122 5,2122" fill="var(--dem-side)"/>
    <rect x="30" y="1722" width="30" height="400" fill="var(--dem)"/>
    <polygon points="5,1714 30,1722 60,1722 35,1714" fill="var(--dem-cap)"/>
    <text class="bar-label" transform="translate(-47,1752) rotate(15)">80%</text>
    <text class="bar-label" transform="translate(32,1740) rotate(-15)">82%</text>
  </g>
</svg>

<div class="cat" style="left:152px">Engage in<br>social<br>distancing</div>
<div class="cat" style="left:278px">Work from<br>home</div>
<div class="cat" style="left:397px">Avoid large<br>gatherings</div>
<div class="cat" style="left:516px">Cancel social<br>activities</div>
<div class="cat small" style="left:635px">Put distance<br>between yourself<br>and other people</div>
<div class="cat" style="left:755px">Wash hands<br>atleast<br>20 seconds</div>
<div class="cat" style="left:875px">Use hand<br>sanitizer</div>
<div class="cat small" style="left:995px">Avoid touching<br>your eyes, nose,<br>and mouth</div>

<div class="legend" style="left:268px"><span class="swatch" style="background:var(--rep)"></span>Corvantist</div>
<div class="legend" style="left:757px"><span class="swatch" style="background:var(--dem)"></span>Halmerite</div>

<p class="footnote">*Based on a survey of 400 U.S. adults conducted March 20 – 24th, 2020.</p>

</body>
</html>
```